Urine collection cup with and without sterile seal sticker

Hello. We need a urine cup label designed please with

Name:
Date of Birth:
Date:
Time:
Temp℃:
Specimen ID:

Product code: TUB-47
Volume markings (e.g., 30 mL, 60 mL, 90 mL).
Vela Drug Tests logo

Could you please provide one version with the additional sterile sticker extending to the top, and one version without the additional sterile sticker?

```html
<!DOCTYPE html>
<html lang="en">
<head>
<meta charset="utf-8">
<title>Vela Drug Tests – Urine Cup Labels</title>
<link href="https://fonts.googleapis.com/css2?family=Roboto:wght@400;500;700;900&display=swap" rel="stylesheet">
<style>
  :root {
    --backdrop: #3b3b3b;
    --label-blue: #28a2e5;
    --ink-blue: #174e8e;
    --paper: #ffffff;
  }
  * { box-sizing: border-box; margin: 0; padding: 0; }
  html, body {
    width: 1200px; height: 900px; overflow: hidden;
    background: var(--backdrop);
    font-family: "Roboto", Arial, sans-serif;
  }
  .canvas { position: relative; width: 1200px; height: 900px; }

  .label-body {
    position: absolute;
    top: 384px;
    height: 393px;
    background: var(--label-blue);
    border-radius: 22px;
  }
  .label-body--sealed { left: 145px; width: 442px; }
  .label-body--plain { left: 682px; width: 373px; }

  .sterile-tab {
    position: absolute;
    left: 492px; top: 121px;
    width: 95px; height: 656px;
    background: var(--label-blue);
    border-radius: 20px;
    z-index: 1;
  }
  .sterile-tab__text {
    position: absolute;
    left: 47px; top: 136px;
    transform: translate(-50%, -50%) rotate(-90deg);
    color: var(--paper);
    font-weight: 700;
    font-size: 52px;
    line-height: 1;
    letter-spacing: 0.5px;
    white-space: nowrap;
  }

  .label-panel {
    position: absolute;
    top: 23px; left: 23px;
    width: 324px; height: 347px;
    background: var(--paper);
    border-radius: 14px;
    padding: 42px 25px 0 26px;
    color: var(--ink-blue);
    z-index: 2;
  }
  .label-body--sealed { z-index: 2; }
  .label-body--plain .label-panel { left: 25px; }

  .field {
    display: flex;
    align-items: flex-end;
    height: 30px;
    font-size: 13.5px;
    font-weight: 700;
    line-height: 1;
  }
  .field__label { white-space: nowrap; margin-right: 8px; }
  .field__line {
    flex: 1;
    border-bottom: 1px solid var(--ink-blue);
    margin-bottom: 2px;
  }
  .field--gap { margin-top: 32px; }

  .product-code {
    position: absolute;
    left: 26px; top: 290px;
    font-size: 13.5px;
    line-height: 19px;
  }
  .product-code__id { font-weight: 400; }
  .product-code__volume { font-weight: 700; }

  .brand {
    position: absolute;
    right: 18px; top: 312px;
    display: flex; align-items: center; gap: 6px;
    font-size: 12px; font-weight: 700;
    color: var(--ink-blue);
  }
  .brand__dot {
    width: 14px; height: 14px; border-radius: 50%;
    background: var(--label-blue);
  }
</style>
</head>
<body>
<main class="canvas">

  <!-- Version with sterile seal tab -->
  <div class="sterile-tab"><span class="sterile-tab__text">STERILE</span></div>
  <section class="label-body label-body--sealed">
    <div class="label-panel">
      <div class="field"><span class="field__label">Name:</span><span class="field__line"></span></div>
      <div class="field"><span class="field__label">Date of Birth:</span><span class="field__line"></span></div>
      <div class="field"><span class="field__label">Date:</span><span class="field__line"></span></div>
      <div class="field"><span class="field__label">Time:</span><span class="field__line"></span></div>
      <div class="field field--gap"><span class="field__label">Temp°C:</span><span class="field__line"></span></div>
      <div class="field"><span class="field__label">Specimen&nbsp; ID:</span><span class="field__line"></span></div>
      <div class="product-code">
        <div class="product-code__id">TUB-47</div>
        <div class="product-code__volume">30 mL</div>
      </div>
      <div class="brand"><span class="brand__dot"></span>Vela Drug Tests</div>
    </div>
  </section>

  <!-- Version without sterile seal tab -->
  <section class="label-body label-body--plain">
    <div class="label-panel">
      <div class="field"><span class="field__label">Name:</span><span class="field__line"></span></div>
      <div class="field"><span class="field__label">Date of Birth:</span><span class="field__line"></span></div>
      <div class="field"><span class="field__label">Date:</span><span class="field__line"></span></div>
      <div class="field"><span class="field__label">Time:</span><span class="field__line"></span></div>
      <div class="field field--gap"><span class="field__label">Temp°C:</span><span class="field__line"></span></div>
      <div class="field"><span class="field__label">Specimen&nbsp; ID:</span><span class="field__line"></span></div>
      <div class="product-code">
        <div class="product-code__id">TUB-47</div>
        <div class="product-code__volume">30 mL</div>
      </div>
      <div class="brand"><span class="brand__dot"></span>Vela Drug Tests</div>
    </div>
  </section>

</main>
</body>
</html>
```